Website Design for a Law Firm

We require a fully functional Website that will be added features such as live chat, Online payment system and online forms. We need to be able to edit the website and update it regularly. We have made a website structure that is attached below.

The website footer must have:
Liability limited by a Scheme approved under Professional Standards Legislation. All legal practitioners employed by Brantley Lawyers Pty Limited (including those described as Principal Solicitor) are members of the Scheme.

Target Market(s)

People seeking legal services in Australia

Industry/Entity Type

Legal

Coding

Coded - Design and coding required

Number of Pages Required

1 page

Requirements
Must have
• Online portal function where clients can upload documents; website that would work perfectly on standard mobile, tablet, laptop, and desktop sizes; the website must have an online payment system.
Nice to have
• Online portal function where clients

```html
<!DOCTYPE html>
<html lang="en">
<head>
<meta charset="utf-8">
<title>Brantley Lawyers</title>
<link rel="stylesheet" href="https://fonts.googleapis.com/css2?family=Baskervville:wght@400;700&family=Open+Sans:wght@400;600&display=swap">
<style>
:root{
  --gold:#c9a55c;
  --gold-light:#d8bb7f;
  --green:#0d2a22;
  --ink:#222;
  --muted:#555;
  --panel:#f4f4f4;
  --white:#fff;
}
*{margin:0;padding:0;box-sizing:border-box}
html,body{width:1200px;height:3409px;overflow:hidden}
body{position:relative;background:var(--white);font-family:"Baskervville",Georgia,serif;color:var(--ink)}
.abs{position:absolute}
.btn{position:absolute;display:flex;align-items:center;justify-content:center;border-radius:16px;font-size:12px;color:var(--white);white-space:nowrap}
.btn-green{background:var(--green)}
.btn-gold{background:var(--gold)}
.brand{font-family:"Baskervville",Georgia,serif;font-weight:700;color:var(--green);letter-spacing:1px;line-height:1}
.brand-ring{position:absolute;border:2px solid var(--gold);border-radius:50%}

/* header */
.site-header{position:absolute;left:0;top:0;width:1200px;height:106px;background:var(--white)}
.call{left:598px;top:28px;font-size:11.5px;color:var(--gold)}
.call b{color:var(--ink);font-weight:400}
.nav a{position:absolute;top:72px;font-size:12.5px;color:var(--ink);text-decoration:none;white-space:nowrap}
.nav a.active{color:var(--gold)}
.dropdown{position:absolute;left:486px;top:106px;width:137px;height:96px;background:var(--gold);padding:12px 12px;z-index:3}
.dropdown p{font-size:9px;color:var(--white);line-height:18.6px;white-space:nowrap}
.dropdown p.u{text-decoration:underline}

/* hero */
.hero{position:absolute;left:0;top:106px;width:1200px;height:487px;background:linear-gradient(100deg,#3b3a38 0%,#6b6459 35%,#4a4640 60%,#2f2d2b 100%)}
.hero h1{position:absolute;left:0;width:1200px;top:176px;text-align:center;font-weight:400;font-size:37px;line-height:43px;color:var(--white)}
.hero h1 b{color:var(--gold);display:block}

.welcome{position:absolute;left:550px;top:530px;width:650px;height:366px;background:var(--gold);color:var(--white);z-index:2}
.welcome h2{position:absolute;left:63px;top:65px;font-size:22px;font-weight:400}
.welcome p{position:absolute;left:63px;width:390px;font-family:"Open Sans",sans-serif;font-size:9px;line-height:18.6px}

.mission{position:absolute;left:200px;top:646px}
.mission h3{font-size:21px;color:var(--gold);font-weight:700}
.mission p{margin-top:6px;font-size:31px;line-height:40px;width:340px}

/* services */
.services{position:absolute;left:0;top:896px;width:1200px;height:679px;background:var(--panel)}
.sec-title{position:absolute;left:0;width:1200px;text-align:center;font-size:30px;font-weight:400}
.hub{position:absolute;left:407px;top:149px;width:386px;height:386px;border-radius:50%;background:var(--white)}
.dot{position:absolute;width:74px;height:74px;margin:-37px 0 0 -37px;border:2px solid var(--gold-light);border-radius:50%;background:var(--white);display:flex;align-items:center;justify-content:center;font-size:26px;color:var(--gold)}
.dot.on{background:var(--gold);color:var(--white);border-color:var(--gold)}
.svc{position:absolute;font-size:18.5px;line-height:24px;white-space:nowrap}
.svc.r{text-align:right}

/* insights */
.photo{position:absolute}
.news-card{position:absolute;left:150px;top:1575px;width:375px;height:416px;background:var(--white)}
.news-card h2{position:absolute;left:50px;top:48px;font-size:30px;font-weight:400}
.date{font-family:"Baskervville",serif;font-size:9.5px;color:var(--gold);font-weight:700;position:absolute}
.news-text{position:absolute;font-size:14.5px;line-height:20px}

/* careers / costs */
.split{position:absolute;left:0;top:2039px;width:1200px;height:249px;overflow:hidden}
.split h2{position:absolute;top:48px;font-size:30px;font-weight:400;color:var(--white)}
.split p{position:absolute;top:108px;width:280px;font-size:14.5px;line-height:20px;color:var(--white)}

/* articles */
.card{position:absolute;top:2422px;width:250px;height:323px;background:var(--panel);border-bottom:3px solid var(--gold)}
.card .img{position:absolute;left:0;top:0;width:250px;height:155px}
.card .date{left:19px;top:177px}
.card .txt{position:absolute;left:19px;top:209px;width:220px;font-size:13.5px;line-height:19px}
.card .more{position:absolute;left:19px;top:277px;font-size:11px;color:var(--gold);display:flex;align-items:center;gap:10px}
.card .arr{width:30px;height:30px;border:1px solid var(--gold-light);border-radius:50%;display:flex;align-items:center;justify-content:center}
.card .arr.on{background:var(--gold)}

/* footer */
.footer{position:absolute;left:0;top:2871px;width:1200px;height:538px;background:var(--panel)}
.footer h4{position:absolute;top:62px;font-size:14.5px;font-weight:700}
.f-item{position:absolute;font-family:"Open Sans",sans-serif;font-size:10px;color:var(--ink)}
.links p{font-family:"Open Sans",sans-serif;font-size:9.5px;line-height:18.7px}
.field{position:absolute;background:var(--white);font-family:"Open Sans",sans-serif;font-size:9.5px;color:var(--muted);padding:9px 12px}
.social{position:absolute;width:30px;height:30px;border-radius:50%;background:var(--green)}
.rule{position:absolute;left:138px;width:924px;height:1px;background:#dcdcdc}
.legal{position:absolute;left:200px;top:356px;width:800px;text-align:center;font-family:"Open Sans",sans-serif;font-size:9px;line-height:18px;color:#444}
.pay{position:absolute;top:459px;width:40px;height:25px;border-radius:3px;border:1px solid #ccc}
</style>
</head>
<body>

<header class="site-header">
  <div class="brand-ring" style="left:167px;top:16px;width:44px;height:44px"></div>
  <div class="brand abs" style="left:130px;top:66px;font-size:18px;text-align:center;width:118px">BRANTLEY<br><span style="font-size:18px">LAWYERS</span></div>
  <div class="abs call">Call us Today at
    <svg width="10" height="10" viewBox="0 0 24 24" style="vertical-align:-1px"><path fill="#c9a55c" d="M6.6 10.8a15 15 0 0 0 6.6 6.6l2.2-2.2c.3-.3.7-.4 1-.2 1.1.4 2.3.6 3.6.6.6 0 1 .4 1 1V20c0 .6-.4 1-1 1A17 17 0 0 1 3 4c0-.6.4-1 1-1h3.5c.6 0 1 .4 1 1 0 1.2.2 2.4.6 3.6.1.3 0 .7-.2 1z"/></svg>
    <b>123-555-0147</b></div>
  <div class="btn btn-green" style="left:787px;top:21px;width:156px;height:31px">Book An Appointments</div>
  <div class="btn btn-gold" style="left:957px;top:21px;width:105px;height:31px">Client Login</div>
  <nav class="nav">
    <a style="left:437px">Home</a>
    <a class="active" style="left:499px">About Us ⌄</a>
    <a style="left:591px">Our Services ⌄</a>
    <a style="left:701px">Insights &amp; News</a>
    <a style="left:819px">Careers</a>
    <a style="left:890px">Costs</a>
    <a style="left:950px">Blog</a>
    <a style="left:1004px">Contact Us</a>
  </nav>
</header>
<div class="dropdown">
  <p>Our History</p><p>Our Promise To You</p><p class="u">Our People</p><p>Mission &amp; Vision Statement</p>
</div>

<section class="hero" role="img" aria-label="Photo of four lawyers in a meeting around a table">
  <h1>Hard work delivers <b>elite results</b></h1>
  <div class="btn btn-gold" style="left:545px;top:284px;width:111px;height:29px">Contact Us</div>
</section>

<section class="welcome">
  <h2>Welcome to <b>Brantley Lawyers</b></h2>
  <p style="top:112px">Lorem Ipsum is simply dummy text of the printing and typesetting industry. Lorem Ipsum has been the industry's standard dummy text ever since the 1500s, when an unknown printer took a galley of type and scrambled it to make a type specimen book.</p>
  <p style="top:205px">If you are going to use a passage of Lorem Ipsum, you need to be sure there isn't anything embarrassing hidden in the middle of text ...</p>
  <div class="btn btn-green" style="left:63px;top:270px;width:112px;height:30px">Explore More</div>
</section>

<section class="mission">
  <h3>Mission &amp; Vision Statement</h3>
  <p>Lorem Ipsum is <b>simply dummy text</b> of the printing and <b>typesetting industry</b> Ipsum.</p>
</section>

<section class="services">
  <h2 class="sec-title" style="top:66px">Our <b>services</b></h2>
  <div class="hub">
    <div class="brand-ring" style="left:146px;top:105px;width:94px;height:94px;border-width:4px"></div>
    <div class="brand abs" style="left:0;width:386px;top:218px;text-align:center;font-size:42px">BRANTLEY</div>
    <div class="brand abs" style="left:0;width:386px;top:266px;text-align:center;font-size:18px;letter-spacing:9px">LAWYERS</div>
  </div>
  <div class="dot" style="left:499px;top:186px">a.</div>
  <div class="dot" style="left:700px;top:186px">b.</div>
  <div class="dot on" style="left:431px;top:280px">c.</div>
  <div class="dot" style="left:769px;top:280px">d.</div>
  <div class="dot" style="left:418px;top:399px">e.</div>
  <div class="dot" style="left:781px;top:399px">f.</div>
  <div class="dot" style="left:499px;top:498px">g.</div>
  <div class="dot" style="left:700px;top:498px">h.</div>
  <div class="svc r" style="right:757px;top:174px">Administrative law</div>
  <div class="svc" style="left:756px;top:174px">Commercial Law</div>
  <div class="svc r" style="right:826px;top:268px;color:var(--gold);text-decoration:underline">Property Law</div>
  <div class="svc" style="left:825px;top:268px">Immigration Law</div>
  <div class="svc r" style="right:838px;top:387px">Employment Law</div>
  <div class="svc" style="left:837px;top:374px">Family &amp; Relationship<br>Law</div>
  <div class="svc r" style="right:761px;top:486px">Criminal</div>
  <div class="svc" style="left:756px;top:486px">Professional Misconduct</div>
  <div class="btn btn-gold" style="left:523px;top:587px;width:154px;height:29px">Book An Appointments</div>
</section>

<section>
  <div class="photo" style="left:0;top:1575px;width:525px;height:416px;background:linear-gradient(90deg,#b9b3a4,#ddd8cc)" role="img" aria-label="Photo of brass scales of justice"></div>
  <div class="photo" style="left:525px;top:1575px;width:675px;height:416px;background:linear-gradient(110deg,#9aa4ad 0%,#c9ccce 50%,#7f8a94 100%)" role="img" aria-label="Photo of a judge's gavel resting on a law book"></div>
  <div class="abs" style="left:138px;top:1575px;width:12px;height:432px;background:var(--gold)"></div>
  <div class="abs" style="left:138px;top:1991px;width:325px;height:16px;background:var(--gold)"></div>
  <div class="news-card">
    <h2>Insights &amp; <b>news</b></h2>
    <div class="abs" style="left:50px;top:97px;width:124px;height:3px;background:var(--gold)"></div>
    <div class="date" style="left:50px;top:119px">DEC-20-2022</div>
    <div class="news-text" style="left:50px;top:152px;width:290px">Contrary to popular belief, Lorem Ipsum is not simply random text.</div>
    <div class="abs" style="left:50px;top:207px;width:275px;height:1px;background:#e3e3e3"></div>
    <div class="date" style="left:50px;top:233px">DEC-20-2022</div>
    <div class="news-text" style="left:50px;top:266px;width:290px">Contrary to popular belief, Lorem Ipsum is not simply random text.</div>
    <div class="btn btn-green" style="left:50px;top:334px;width:99px;height:28px">See More</div>
  </div>
</section>

<section class="split">
  <div class="abs" style="left:0;top:0;width:1200px;height:249px;background:linear-gradient(90deg,#c09a54,#d6b979)" role="img" aria-label="Photo of hands with a calculator and documents"></div>
  <div class="abs" style="left:0;top:0;width:1200px;height:249px;background:linear-gradient(90deg,#1f3b33,#3d5249);clip-path:polygon(0 0,627px 0,569px 249px,0 249px)" role="img" aria-label="Photo of a handshake over a desk with a gavel"></div>
  <h2 style="left:138px">Careers</h2>
  <p style="left:138px">Contrary to popular belief, lorem ipsum is not simply random text.</p>
  <div class="btn btn-gold" style="left:138px;top:176px;width:111px;height:30px">Find a Job</div>
  <h2 style="left:787px">Costs</h2>
  <p style="left:787px">Contrary to popular belief, lorem ipsum is not simply random text.</p>
  <div class="btn btn-green" style="left:787px;top:176px;width:113px;height:30px">Get a Costs</div>
  <div class="abs" style="left:505px;top:29px;width:190px;height:190px;border-radius:50%;background:var(--white)">
    <div class="brand-ring" style="left:71px;top:38px;width:48px;height:48px"></div>
    <div class="brand abs" style="left:0;width:190px;top:102px;text-align:center;font-size:23px">BRANTLEY</div>
    <div class="brand abs" style="left:0;width:190px;top:129px;text-align:center;font-size:10px;letter-spacing:5px">LAWYERS</div>
  </div>
</section>

<section>
  <h2 class="sec-title" style="top:2353px">Recent <b>articles</b></h2>
  <div class="card" style="left:200px">
    <div class="img" style="background:linear-gradient(135deg,#6b5b4b,#a08a72)" role="img" aria-label="Photo of colleagues discussing at an office desk"></div>
    <div class="date">DEC-20-2022</div>
    <div class="txt">There are many variations lorem Ipsum available ...</div>
    <div class="more">Read More <span class="arr on"><svg width="8" height="8" viewBox="0 0 8 8"><path d="M3 1l3 3-3 3" stroke="#fff" fill="none"/></svg></span></div>
  </div>
  <div class="card" style="left:475px">
    <div class="img" style="background:linear-gradient(135deg,#5a5048,#9c9690)" role="img" aria-label="Photo of a gavel beside a laptop and glasses"></div>
    <div class="date">JAN-12-2023</div>
    <div class="txt">There are many variations lorem Ipsum available ...</div>
    <div class="more">Read More <span class="arr"><svg width="8" height="8" viewBox="0 0 8 8"><path d="M3 1l3 3-3 3" stroke="#c9a55c" fill="none"/></svg></span></div>
  </div>
  <div class="card" style="left:750px">
    <div class="img" style="background:linear-gradient(135deg,#3e3128,#8a6e55)" role="img" aria-label="Photo of a person signing documents at a desk"></div>
    <div class="date">FEB-14-2023</div>
    <div class="txt">There are many variations lorem Ipsum available ...</div>
    <div class="more">Read More <span class="arr"><svg width="8" height="8" viewBox="0 0 8 8"><path d="M3 1l3 3-3 3" stroke="#c9a55c" fill="none"/></svg></span></div>
  </div>
  <div class="btn btn-green" style="left:550px;top:2778px;width:100px;height:30px">View All</div>
</section>

<footer class="footer">
  <h4 style="left:138px">Contact Us</h4>
  <h4 style="left:344px">Quick Links</h4>
  <h4 style="left:512px">Our Services</h4>
  <h4 style="left:713px">Book An Appointments</h4>

  <svg class="abs" style="left:138px;top:111px" width="11" height="11" viewBox="0 0 24 24"><path fill="#c9a55c" d="M6.6 10.8a15 15 0 0 0 6.6 6.6l2.2-2.2c.3-.3.7-.4 1-.2 1.1.4 2.3.6 3.6.6.6 0 1 .4 1 1V20c0 .6-.4 1-1 1A17 17 0 0 1 3 4c0-.6.4-1 1-1h3.5c.6 0 1 .4 1 1 0 1.2.2 2.4.6 3.6.1.3 0 .7-.2 1z"/></svg>
  <div class="f-item" style="left:156px;top:107px;font-family:'Baskervville',serif;font-size:14px">123-555-0147</div>
  <svg class="abs" style="left:138px;top:145px" width="11" height="9" viewBox="0 0 22 16"><rect x="1" y="1" width="20" height="14" fill="#c9a55c"/><path d="M1 1l10 8 10-8" stroke="#fff" fill="none" stroke-width="1.5"/></svg>
  <div class="f-item" style="left:156px;top:142px">info@brantleylawyers.com</div>
  <svg class="abs" style="left:138px;top:175px" width="9" height="12" viewBox="0 0 18 24"><path fill="#c9a55c" d="M9 0a9 9 0 0 0-9 9c0 7 9 15 9 15s9-8 9-15a9 9 0 0 0-9-9zm0 12a3 3 0 1 1 0-6 3 3 0 0 1 0 6z"/></svg>
  <div class="f-item" style="left:156px;top:172px;line-height:18.6px">Lorem 302, 3. kat,<br>G 2 Zgrada br. 03 Lorem ipsum,<br>Dolor, Sit-Amet, 12345</div>
  <div class="social" style="left:137px;top:243px"></div>
  <div class="social" style="left:176px;top:243px;background:var(--gold)"></div>
  <div class="social" style="left:213px;top:243px"></div>

  <div class="abs links" style="left:344px;top:102px"><p>Home</p><p>About Us</p><p>Our Services</p><p>Insights &amp; News</p><p>Careers</p><p>Costs</p><p>Blog</p><p>Contact Us</p><p>Online pay</p></div>
  <div class="abs links" style="left:512px;top:102px"><p>Administrative law</p><p>Commercial Law</p><p>Property Law</p><p>Immigration Law</p><p>Employment Law</p><p>Family &amp; Relationship Law</p><p>Criminal</p><p>Professional Misconduct</p></div>

  <div class="field" style="left:713px;top:107px;width:168px;height:29px">Name</div>
  <div class="field" style="left:894px;top:107px;width:168px;height:29px">Phone</div>
  <div class="field" style="left:713px;top:151px;width:349px;height:29px">Email</div>
  <div class="field" style="left:713px;top:194px;width:349px;height:61px">Message</div>
  <div class="btn btn-gold" style="left:713px;top:270px;width:86px;height:29px">Send</div>

  <div class="abs" style="left:1099px;top:-32px;width:64px;height:64px;border-radius:50%;background:var(--gold);display:flex;align-items:center;justify-content:center">
    <svg width="26" height="26" viewBox="0 0 24 24"><path fill="#fff" d="M3 3h18v14H7l-4 4z"/><path d="M8 12l5-5 2 2-5 5H8z" fill="#c9a55c"/></svg>
  </div>

  <div class="rule" style="top:331px"></div>
  <p class="legal">Liability limited by a Scheme approved under Professional Standards Legislation. All legal practitioners employed by Brantley Lawyers Pty Limited (including those described as Principal Solicitor) are members of the Scheme.</p>
  <div class="rule" style="top:435px"></div>

  <div class="brand-ring" style="left:138px;top:440px;width:60px;height:60px;border-width:3px"></div>
  <div class="f-item" style="left:232px;top:464px">© 2023 <span style="color:var(--gold)">Brantley Lawyers</span>. All Right Reserved</div>
  <div class="f-item" style="left:512px;top:464px">Compliance &nbsp;&nbsp; / &nbsp;&nbsp; Disclaimers</div>
  <div class="f-item" style="left:713px;top:462px;font-family:'Baskervville',serif;font-size:12px;font-weight:700">We Accept</div>
  <div class="pay" style="left:787px;background:#fff"></div>
  <div class="pay" style="left:832px;background:#fff"></div>
  <div class="pay" style="left:876px;background:#d9433a;border-color:#d9433a"></div>
  <div class="pay" style="left:920px;background:#2d58a5;border-color:#2d58a5"></div>
  <div class="pay" style="left:965px;background:#f0d98a;border-color:#e0c66e"></div>
</footer>

</body>
</html>
```